Website Design for Business Law Firm

We have a logo and now we would like a web site design for our new website. Our small firm provides creative and aggressive transactional (not litigation) legal services to advise healthcare, technology, internet-based and traditional companies and investors in such companies on healthcare, technology, financing, mergers/acquisitions, real estate and other transactions, legal compliance and general corporate and business matters.

We would like to see a website design that is professional and appropriate for executives, professionals, investors and government regulators to visit, that conveys professionalism and competence while being a little edgy and modern - no typical legal motifs such as gavels, books, or scales of justice. We advise businesses and investors and guide them through complicated issues quickly, capably and differently from other law firms. We are part of the business team and get things done.

The logo is attached, and we like gray as a color to complement it. The intention of the logo is to convey that in a storm or challenging time, people come to this firm, and people come to this firm when they need the power and disruption to change things or shake them up.

I have also enclosed a picture of our business card for consideration.

On the other hand, you can check out the current simple site at www.venhollow.example to see we have used a space motif in the past to evoke that we help create stars (the nebula featured there). This is not a necessary part of the new website and it may look better without it.

We appreciate your creativity and look forward to designs.

Industry/Entity Type

Business

Requirements
Must have
• We anticipate the following pages, and you may submit different ideas for the different pages:
• 1. Landing page
• 2. Services pages - healthcare, IT/Technology, general counsel services, financings, mergers/acquisitions, mediation/arbitration, procurement and productization
• 3. About Us including contact information
• Our name and contact information:
• Quellane Law Firm, P.C.
• 8716 SW 19th Ave.
• Portland, OR 97213
• phone: 971.555.0143
• fax: 971.555.0187
Nice to have
• Please consider designs that enhance the impressions we are looking for
Should not have
• Please no gavels, scales of justice, law books, or similar traditional legal imagery.

```html
<!DOCTYPE html>
<html lang="en">
<head>
<meta charset="utf-8">
<title>Quellane Law Firm, P.C.</title>
<link rel="stylesheet" href="https://fonts.googleapis.com/css2?family=Oswald:wght@300;400&family=Lato:wght@400&display=swap">
<style>
  :root {
    --nav-bg: #222324;
    --nav-text: #f2f2f2;
    --space-deep: #1c1d24;
    --space-mid: #3a3a44;
    --space-glow: #6e625c;
    --band-gray: rgba(102, 122, 128, 0.82);
    --accent: rgba(156, 40, 82, 0.82);
    --white: #ffffff;
  }
  * { box-sizing: border-box; margin: 0; padding: 0; }
  html, body {
    width: 1200px;
    height: 597px;
    overflow: hidden;
    background: var(--space-deep);
  }
  .page {
    position: relative;
    width: 1200px;
    height: 597px;
    overflow: hidden;
    font-family: "Lato", Arial, sans-serif;
    color: var(--white);
  }
  .site-header {
    position: absolute;
    top: 0; left: 0;
    width: 1200px;
    height: 83px;
    background: var(--nav-bg);
    z-index: 2;
  }
  .brand {
    position: absolute;
    left: 124px;
    top: 11px;
    height: 60px;
    display: flex;
    align-items: center;
    gap: 12px;
    font-family: "Lato", Arial, sans-serif;
    font-size: 26px;
    letter-spacing: 6px;
    color: var(--nav-text);
  }
  .brand-mark {
    width: 40px;
    height: 40px;
    background: #5f7c80;
  }
  .main-nav {
    position: absolute;
    right: 138px;
    top: 0;
    height: 64px;
    display: flex;
    align-items: center;
    gap: 25px;
  }
  .main-nav a {
    font-size: 15px;
    color: var(--nav-text);
    text-decoration: none;
    letter-spacing: -0.2px;
  }
  .space-backdrop {
    position: absolute;
    top: 83px; left: 0;
    width: 1200px;
    height: 514px;
    background:
      radial-gradient(ellipse 260px 200px at 600px 260px, var(--space-glow) 0%, rgba(110,98,92,0.4) 45%, transparent 75%),
      radial-gradient(ellipse 700px 420px at 600px 260px, var(--space-mid) 0%, var(--space-deep) 80%);
  }
  .hero {
    position: absolute;
    top: 83px; left: 0;
    width: 1200px;
    height: 331px;
    text-align: center;
    background: rgba(20, 20, 26, 0.25);
  }
  .hero-title {
    position: absolute;
    top: 50px;
    width: 100%;
    font-family: "Oswald", Arial, sans-serif;
    font-weight: 300;
    font-size: 72px;
    line-height: 1;
    letter-spacing: 0.5px;
  }
  .hero-tagline {
    position: absolute;
    top: 149px;
    width: 100%;
    font-size: 20px;
  }
  .hero-actions {
    position: absolute;
    top: 215px;
    width: 100%;
    display: flex;
    justify-content: center;
    gap: 13px;
  }
  .button {
    display: inline-block;
    height: 36px;
    padding: 0 13px;
    line-height: 36px;
    font-size: 15px;
    color: var(--white);
    background: var(--accent);
    text-decoration: none;
  }
  .services {
    position: absolute;
    top: 414px; left: 0;
    width: 1200px;
    height: 183px;
    background: var(--band-gray);
    text-align: center;
  }
  .services-title {
    position: absolute;
    top: 40px;
    width: 100%;
    font-family: "Oswald", Arial, sans-serif;
    font-weight: 300;
    font-size: 40px;
    line-height: 1;
  }
  .services-intro {
    position: absolute;
    top: 124px;
    left: 120px;
    width: 960px;
    font-size: 18.5px;
    line-height: 27px;
  }
</style>
</head>
<body>
<div class="page">
  <header class="site-header">
    <div class="brand"><span class="brand-mark"></span>QUELLANE</div>
    <nav class="main-nav">
      <a href="#">Home</a>
      <a href="#">Services</a>
      <a href="#">Newsletter</a>
      <a href="#">About</a>
      <a href="#">Gallery</a>
      <a href="#">Contact</a>
    </nav>
  </header>

  <div class="space-backdrop" role="img" aria-label="Photograph of a spiral galaxy with bright stars in deep space"></div>

  <section class="hero">
    <h1 class="hero-title">QUELLANE</h1>
    <p class="hero-tagline">The law firm that stars are made of!</p>
    <div class="hero-actions">
      <a class="button" href="#">Services</a>
      <a class="button" href="#">Contact Us</a>
    </div>
  </section>

  <section class="services">
    <h2 class="services-title">Services</h2>
    <p class="services-intro">This section can bring the users attention to your main services, research shows that 4 selling points is about as much as anyone can take in effectively.</p>
  </section>
</div>
</body>
</html>
```